We want a business card/punch card for our business. We are including examples of our current business card (we like the front of our business card and not looking to remake it). We need only back side to be designed in form of a punch card (we are including a sample of the punch card we made, but are unsatisfied). For each $180 spend (9 punches) our clients have $20 off.

Colors
886aae

```html
<!DOCTYPE html>
<html lang="en">
<head>
<meta charset="utf-8">
<title>Lunaris Arts – Business Card &amp; Punch Card</title>
<link rel="stylesheet" href="https://fonts.googleapis.com/css2?family=Mulish:wght@400;500;600&display=swap">
<style>
  :root {
    --page: #eceef1;
    --purple: #5b2e93;
    --violet: #886aae;
    --blue: #5a5fb8;
    --periwinkle: #7b82d0;
    --lavender-deep: #b9c0ea;
    --lavender-light: #eef0fb;
    --stamp: #c9cdf0;
    --white: #ffffff;
  }
  * { margin: 0; padding: 0; box-sizing: border-box; }
  html, body {
    width: 1154px; height: 1200px; overflow: hidden;
    background: var(--page);
    font-family: "Mulish", "Helvetica Neue", Arial, sans-serif;
  }
  .canvas { position: relative; width: 1154px; height: 1200px; }
  .card {
    position: absolute; left: 97px; width: 960px; height: 549px;
    border-radius: 28px; overflow: hidden;
    box-shadow: 0 6px 18px rgba(40, 30, 80, 0.18);
  }
  .card-front { top: 30px; }
  .card-back { top: 621px; }
  .card-bg { position: absolute; inset: 0; width: 100%; height: 100%; }
  .text-light { color: var(--white); position: absolute; }

  /* Front */
  .brand {
    position: absolute; left: 70px; top: 370px;
    display: flex; align-items: center; gap: 18px;
    color: var(--blue); font-weight: 600; font-size: 62px; letter-spacing: 0.5px;
  }
  .brand-dot { width: 34px; height: 34px; border-radius: 50%; background: var(--blue); }
  .contact-name { right: 70px; top: 62px; font-size: 34px; font-weight: 500; }
  .contact-phone { right: 70px; top: 106px; font-size: 31px; }
  .contact-web { right: 60px; top: 322px; font-size: 24px; text-align: right; line-height: 1.35; }
  .contact-social { right: 50px; top: 440px; font-size: 24px; text-align: right; line-height: 1.6; }

  /* Back */
  .frame {
    position: absolute; left: 30px; top: 28px; right: 30px; bottom: 28px;
    border: 1.5px dashed rgba(255,255,255,0.7);
  }
  .divider {
    position: absolute; left: 518px; top: 28px; bottom: 28px;
    border-left: 1.5px dashed rgba(255,255,255,0.7);
  }
  .punch-grid { position: absolute; left: 0; top: 0; width: 518px; height: 549px; }
  .services {
    left: 518px; right: 30px; top: 58px;
    text-align: center; font-size: 20.5px; line-height: 31px;
  }
  .services .rule { border-top: 1.5px dotted rgba(255,255,255,0.65); margin: 3px 40px; }
  .services .sep { display: inline-block; width: 8px; height: 8px; border: 2px solid var(--white); border-radius: 50%; margin: 0 6px; vertical-align: middle; }
  .appreciation {
    left: 538px; right: 40px; top: 290px;
    text-align: center; font-size: 20.5px; line-height: 27px; font-weight: 500;
  }
  .appreciation strong { font-weight: 600; }
</style>
</head>
<body>
<main class="canvas">

  <section class="card card-front" aria-label="Business card front">
    <svg class="card-bg" viewBox="0 0 960 549" preserveAspectRatio="none" aria-hidden="true">
      <defs>
        <linearGradient id="front-lavender" x1="0" y1="0" x2="1" y2="1">
          <stop offset="0" stop-color="var(--lavender-deep)"/>
          <stop offset="1" stop-color="var(--lavender-light)"/>
        </linearGradient>
      </defs>
      <rect width="960" height="549" fill="var(--purple)"/>
      <path d="M520 549 C620 390 770 300 960 275 L960 549 Z" fill="var(--blue)"/>
      <path d="M600 0 C520 130 560 330 500 549 L540 549 C600 330 560 130 650 0 Z" fill="var(--periwinkle)" opacity="0.8"/>
      <path d="M0 0 L575 0 C490 130 535 330 475 549 L0 549 Z" fill="url(#front-lavender)"/>
    </svg>
    <div role="img" aria-label="Soft lavender mandala pattern behind the brand name" style="position:absolute;left:0;top:0;width:500px;height:549px;"></div>
    <div class="brand"><span class="brand-dot"></span>Lunaris Arts</div>
    <p class="text-light contact-name">Selene Amaris</p>
    <p class="text-light contact-phone">555-204-7781</p>
    <p class="text-light contact-web">www.lunarisarts.com<br>hello@lunarisarts.com</p>
    <p class="text-light contact-social">Friendsphere.com/LunarisArts<br>Gatherly.com/Lunaris-Arts</p>
  </section>

  <section class="card card-back" aria-label="Punch card back">
    <svg class="card-bg" viewBox="0 0 960 549" preserveAspectRatio="none" aria-hidden="true">
      <rect width="960" height="549" fill="var(--purple)"/>
      <path d="M0 549 L0 330 C300 250 700 235 960 255 L960 549 Z" fill="var(--blue)"/>
      <path d="M250 0 C150 140 60 260 0 420 L0 470 C80 290 190 150 300 0 Z" fill="var(--periwinkle)" opacity="0.55"/>
      <path d="M320 0 C200 150 100 290 20 549 L60 549 C140 300 240 160 350 0 Z" fill="var(--violet)" opacity="0.4"/>
    </svg>
    <div class="frame"></div>
    <div class="divider"></div>
    <svg class="punch-grid" viewBox="0 0 518 549" role="img" aria-label="Nine punch spots, each a decorative rosette with a blank centre">
      <g fill="var(--stamp)">
        <circle cx="123" cy="103" r="62"/><circle cx="280" cy="103" r="62"/><circle cx="437" cy="103" r="62"/>
        <circle cx="123" cy="270" r="62"/><circle cx="280" cy="270" r="62"/><circle cx="437" cy="270" r="62"/>
        <circle cx="123" cy="437" r="62"/><circle cx="280" cy="437" r="62"/><circle cx="437" cy="437" r="62"/>
      </g>
      <g fill="var(--white)">
        <circle cx="123" cy="103" r="28"/><circle cx="280" cy="103" r="28"/><circle cx="437" cy="103" r="28"/>
        <circle cx="123" cy="270" r="28"/><circle cx="280" cy="270" r="28"/><circle cx="437" cy="270" r="28"/>
        <circle cx="123" cy="437" r="28"/><circle cx="280" cy="437" r="28"/><circle cx="437" cy="437" r="28"/>
      </g>
    </svg>
    <div class="text-light services">
      <p>Tantra<span class="sep"></span>Tao<span class="sep"></span>Yoga<span class="sep"></span>Tai Chi<span class="sep"></span>Reiki</p>
      <div class="rule"></div>
      <p>Sacred Sexuality<span class="sep"></span>Sexual Healing</p>
      <p>Sound Healing<span class="sep"></span>Energy Work<span class="sep"></span>Rituals</p>
      <div class="rule"></div>
      <p>Partners Yoga<span class="sep"></span>Four Hands Massage</p>
    </div>
    <p class="text-light appreciation">
      This card is a symbol of appreciation from us to you. Without your business, we would not be able to do what we love most!<br>
      When you fill out this card, you will receive <strong>$20</strong> towards your next Weekly Event, Workshop, or Private Session.
    </p>
  </section>

</main>
</body>
</html>
```